quillcrestPRESS is launching 2 new eBooks and needs beautiful and compelling cover designs and a desig

We are launching 2 non-fiction eBooks that are part of a series but will be launched separately, so we would like to see some continuity between the 2 designs - but each should have a strong stand alone identity.

The eBooks are both in the naturopathic/holistic health niche.

ebook 1 title is:
Shaping Your Perfect Studio
(sub) The Wellness Manual to growing your own thriving natural and
alternative therapy business.

The book is a comprehensive guide for naturopaths and other alternative health providers - ( Naturopath,
Nutritionist, Homeopath, Acupuncturist, Chiropractor,
Massage Therapist, or Holistic Health Specialist), who are seeking to setup their own, profitable naturopathic business.

ebook 2 title is:
Silver Handshakes (subtitle) Win 40 + Patients Inside Six Weeks

(sub/sub)27 methods to promote your natural and alternative therapy business

This book is a list of 32 tips for the same audience to increase there customer referrals (and therefore income).

Each book should feature
written by Moira Tennant
published by Tennant Publishing

Each book should feature the authors photograph on the cover (attached) - no caveats on cropping etc - whatever fits with the design.

You can see more about the writer on her website here:

http://www.harbourleafwellness.example.au/

What we require:

1) cover art for both eBooks that conforms to Kindle and iPad specs
2) Flat & 3D book cover art for use on website and marketing campaigns
3) we will require layered PSD files on completion of project.

I'd like to add that we are seeking to build a relationship with the designer we choose for this project, as we are publishing many other titles throughout 2014

Many eBook writers jump straight to Gigly for a cover. The result is most self published books have the same generic look the 'gigly' look.

I don't want that look.

We want to reward great design and ensure quillcrestPRESS eBook titles have a great look.

The winning designer will be working with us on many more projects.

Colin Marsh
quillcrestPRESS

```html
<!DOCTYPE html>
<html lang="en">
<head>
<meta charset="utf-8">
<title>Shaping Your Perfect Studio — Cover</title>
<link rel="stylesheet" href="https://fonts.googleapis.com/css2?family=Cormorant+SC:wght@500;600&family=Junge&display=swap">
<style>
  :root {
    --leaf: #6aa51c;
    --leaf-deep: #2f6b3a;
    --band: #6aaa12;
    --paper: #ffffff;
    --ink-white: #ffffff;
    --steel-light: #eef0f2;
    --steel-mid: #c9ccd3;
    --tube-green: #8cc63f;
    --portrait-warm: #c9a88c;
    --portrait-cool: #5a4a52;
  }
  html, body {
    margin: 0;
    padding: 0;
    width: 820px;
    height: 1200px;
    overflow: hidden;
    background: var(--paper);
  }
  .cover {
    position: relative;
    width: 820px;
    height: 1200px;
    background: var(--paper);
    overflow: hidden;
    font-family: "Junge", Georgia, serif;
    color: var(--leaf);
  }
  .cover__title {
    position: absolute;
    top: 52px;
    left: 0;
    width: 820px;
    margin: 0;
    text-align: center;
    font-family: "Cormorant SC", "Times New Roman", serif;
    font-weight: 500;
    font-size: 50px;
    line-height: 1;
    letter-spacing: 0.3px;
    color: var(--leaf);
    white-space: nowrap;
  }
  .cover__title-initial {
    font-size: 74px;
    color: var(--leaf-deep);
  }
  .cover__subtitle {
    position: absolute;
    top: 172px;
    left: 72px;
    width: 660px;
    margin: 0;
    font-size: 24px;
    line-height: 1.8;
    text-align: justify;
    text-align-last: left;
    color: var(--leaf);
  }
  .cover__blurb {
    position: absolute;
    top: 350px;
    left: 76px;
    width: 232px;
    margin: 0;
    font-size: 18px;
    line-height: 1.65;
    text-align: justify;
    hyphens: auto;
    -webkit-hyphens: auto;
    color: var(--leaf);
  }
  .cover__artwork {
    position: absolute;
    top: 335px;
    left: 330px;
    width: 450px;
    height: 440px;
    border-radius: 48px;
    background:
      radial-gradient(ellipse at 70% 70%, var(--tube-green) 0%, rgba(140,198,63,0.35) 40%, rgba(255,255,255,0) 70%),
      linear-gradient(160deg, var(--steel-light) 0%, var(--steel-mid) 45%, #ffffff 100%);
  }
  .cover__band {
    position: absolute;
    top: 0;
    left: 0;
    width: 820px;
    height: 1200px;
  }
  .cover__byline {
    position: absolute;
    top: 898px;
    left: 370px;
    width: 420px;
    margin: 0;
    text-align: center;
    font-size: 38px;
    line-height: 1.2;
    color: var(--ink-white);
    transform: rotate(-12deg);
    transform-origin: center;
  }
  .cover__portrait {
    position: absolute;
    top: 875px;
    left: 118px;
    width: 240px;
    height: 240px;
    border-radius: 50%;
    border: 10px solid var(--leaf);
    box-shadow: inset 0 0 0 6px var(--paper);
    background: linear-gradient(170deg, #e9e4df 0%, var(--portrait-warm) 45%, var(--portrait-cool) 100%);
  }
  .cover__publisher {
    position: absolute;
    top: 1085px;
    left: 500px;
    width: 300px;
    margin: 0;
    text-align: center;
    font-size: 28px;
    line-height: 1.25;
    color: var(--leaf-deep);
    transform: rotate(-6deg);
  }
</style>
</head>
<body>
<main class="cover">
  <h1 class="cover__title">Shaping Your <span class="cover__title-initial">P</span>erfect Studio</h1>

  <p class="cover__subtitle">The Wellness Manual to growing your own thriving natural and alternative therapy business.</p>

  <div class="cover__artwork" role="img" aria-label="Photograph of a green stethoscope with a silver chest piece"></div>

  <p class="cover__blurb">The book is a comprehensive guide for naturopaths and other alternative health providers - ( Naturopath, Nutritionist, Homeopath, Acupuncturist, Chiropractor, Massage Therapist, or Holistic Health Specialist), who are seeking to setup their own, profitable naturopathic business.</p>

  <svg class="cover__band" viewBox="0 0 820 1200" aria-hidden="true">
    <polygon points="190,960 820,825 820,965 190,1100" fill="var(--band)"/>
  </svg>

  <p class="cover__byline">Written By<br>Moira Tennant</p>

  <div class="cover__portrait" role="img" aria-label="Portrait photograph of the author, Moira Tennant"></div>

  <p class="cover__publisher">Published By<br>Tennant Publishing</p>
</main>
</body>
</html>
```